I want a business card design. the company is an infrastructure development company.

Target Market(s)

Government
real estate investors
real estate clients

Industry/Entity Type

Business

```html
<!DOCTYPE html>
<html lang="en">
<head>
<meta charset="utf-8">
<title>Granite Vale – Business Card</title>
<link rel="stylesheet" href="https://fonts.googleapis.com/css2?family=Arimo:wght@400;700&display=swap">
<style>
  :root {
    --page-bg: #e9e7e4;
    --card-bg: #f7f7f6;
    --ink: #2e2e2e;
    --ink-soft: #4a4a4a;
    --brand-red: #f0474c;
    --brand-blue: #3cc0ea;
  }
  * { box-sizing: border-box; margin: 0; padding: 0; }
  html, body {
    width: 1200px; height: 576px; overflow: hidden;
    background: var(--page-bg);
    font-family: "Arimo", Arial, sans-serif;
    color: var(--ink);
  }
  .stage {
    width: 1200px; height: 576px;
    display: flex; align-items: center; justify-content: center;
  }
  .business-card {
    position: relative;
    width: 840px; height: 480px;
    background: var(--card-bg);
    box-shadow: 0 10px 30px rgba(0,0,0,.18);
  }
  .brand {
    position: absolute; left: 360px; top: 92px;
    display: flex; align-items: center; gap: 16px;
  }
  .brand-mark {
    width: 34px; height: 34px; background: var(--brand-blue);
  }
  .brand-name {
    font-size: 52px; font-weight: 400; letter-spacing: 2px;
    color: var(--brand-red); line-height: 1;
  }
  .holder { position: absolute; left: 76px; top: 196px; }
  .holder-name { font-size: 27px; letter-spacing: 1.5px; color: var(--ink); }
  .holder-title { margin: 8px 0 0 128px; font-size: 19px; letter-spacing: 1px; }
  .contact-list { list-style: none; position: absolute; }
  .contact-list li {
    display: flex; align-items: flex-start; gap: 12px;
    font-size: 15px; letter-spacing: 1.2px; color: var(--ink-soft);
    line-height: 1.35; margin-bottom: 16px;
  }
  .contact-list svg { flex: none; width: 16px; height: 16px; margin-top: 1px; }
  .personal-contacts { left: 76px; top: 288px; }
  .personal-contacts svg { color: var(--brand-red); }
  .company-contacts { left: 520px; top: 268px; }
  .company-contacts svg { color: var(--brand-blue); }
  .company-contacts li { margin-bottom: 12px; }
</style>
</head>
<body>
<main class="stage">
  <article class="business-card">
    <div class="brand">
      <span class="brand-mark"></span>
      <span class="brand-name">GRANITE VALE</span>
    </div>

    <div class="holder">
      <p class="holder-name">Kolawole Bankole</p>
      <p class="holder-title">MD.</p>
    </div>

    <ul class="contact-list personal-contacts">
      <li><svg viewBox="0 0 16 16" fill="none" stroke="currentColor" stroke-width="1.4"><path d="M3 1.5l2.5 0 1.2 3.2-1.6 1.2a8 8 0 0 0 5 5l1.2-1.6 3.2 1.2v2.5a1.5 1.5 0 0 1-1.6 1.5A12.5 12.5 0 0 1 1.5 3.1 1.5 1.5 0 0 1 3 1.5z"/></svg>+234 8051234407</li>
      <li><svg viewBox="0 0 16 16" fill="none" stroke="currentColor" stroke-width="1.4"><path d="M3 1.5l2.5 0 1.2 3.2-1.6 1.2a8 8 0 0 0 5 5l1.2-1.6 3.2 1.2v2.5a1.5 1.5 0 0 1-1.6 1.5A12.5 12.5 0 0 1 1.5 3.1 1.5 1.5 0 0 1 3 1.5z"/></svg>+234 7039825514</li>
      <li><svg viewBox="0 0 16 16" fill="none" stroke="currentColor" stroke-width="1.4"><rect x="1.5" y="3" width="13" height="10"/><path d="M1.5 3l6.5 5.5L14.5 3"/></svg>kolawole@granitevale.com</li>
    </ul>

    <ul class="contact-list company-contacts">
      <li><svg viewBox="0 0 16 16" fill="none" stroke="currentColor" stroke-width="1.4"><path d="M8 15s5-5 5-8.5a5 5 0 0 0-10 0C3 10 8 15 8 15z"/><circle cx="8" cy="6.5" r="1.8"/></svg><span>12 Palmgrove Street,<br>Off Harbour Link Road,<br>Ikeja Lagos, Nigeria</span></li>
      <li><svg viewBox="0 0 16 16" fill="none" stroke="currentColor" stroke-width="1.4"><path d="M3 1.5l2.5 0 1.2 3.2-1.6 1.2a8 8 0 0 0 5 5l1.2-1.6 3.2 1.2v2.5a1.5 1.5 0 0 1-1.6 1.5A12.5 12.5 0 0 1 1.5 3.1 1.5 1.5 0 0 1 3 1.5z"/></svg>+234 13571209,</li>
      <li><svg viewBox="0 0 16 16" fill="none" stroke="currentColor" stroke-width="1.4"><path d="M3 1.5l2.5 0 1.2 3.2-1.6 1.2a8 8 0 0 0 5 5l1.2-1.6 3.2 1.2v2.5a1.5 1.5 0 0 1-1.6 1.5A12.5 12.5 0 0 1 1.5 3.1 1.5 1.5 0 0 1 3 1.5z"/></svg>+234 7082461135</li>
      <li><svg viewBox="0 0 16 16" fill="none" stroke="currentColor" stroke-width="1.4"><rect x="1.5" y="3" width="13" height="10"/><path d="M1.5 3l6.5 5.5L14.5 3"/></svg>info@granitevale.com</li>
      <li><svg viewBox="0 0 16 16" fill="none" stroke="currentColor" stroke-width="1.4"><circle cx="8" cy="8" r="2.6"/><path d="M10.6 5.5v3.8a1.9 1.9 0 0 0 3.8 0V8a6.4 6.4 0 1 0-2.6 5.2"/></svg>www.granitevale.com</li>
    </ul>
  </article>
</main>
</body>
</html>
```